Builder Supply Needs Eye-catching Poster Design for Upcoming Workshop

We're doing a concrete carving workshop. It's a new concept in our area. We need a poster that will get people asking questions about it.

Needs to have:
- Our logo somewhere
- Picture(s) of concrete carving (attached)
- Should say, "We're hosting a vertical carving workshop. Details to be announced. Sign up for more information"

Target Market(s)

Contractors

Industry/Entity Type

Concrete

Font styles to use
Sans Serif

Requirements
Must have
• - Our logo somewhere
• - Picture(s) of concrete carving (attached)
• - Should say, "We're hosting a vertical carving workshop. Details to be announced. Sign up for more information"
• - Needs to be high enough resolution to be printed at 24 x 36 by Quillo Press
Nice to have
• Eye-catching design

```html
<!DOCTYPE html>
<html lang="en">
<head>
<meta charset="utf-8">
<title>Vertical Carving Workshop Poster</title>
<link href="https://fonts.googleapis.com/css2?family=Open+Sans:wght@400;600;700;800&display=swap" rel="stylesheet">
<style>
  :root {
    --header-top: #cfd2d5;
    --header-bottom: #f1f2f3;
    --ink-dark: #3b3f45;
    --panel-dark: #45484d;
    --panel-darker: #2f3236;
    --accent-blue: #1d8fd8;
    --band-blue: #1c7fc7;
    --band-blue-dark: #1466a6;
    --white: #ffffff;
    --footer-grey: #e4e6e8;
  }
  * { margin: 0; padding: 0; box-sizing: border-box; }
  html, body { width: 874px; height: 1200px; overflow: hidden; }
  body { font-family: "Open Sans", Arial, sans-serif; background: var(--footer-grey); }
  .poster { position: relative; width: 874px; height: 1200px; background: var(--footer-grey); }

  .poster-header {
    position: absolute; left: 0; top: 0; width: 874px; height: 252px;
    background: linear-gradient(180deg, var(--header-top), var(--header-bottom));
  }
  .brand { position: absolute; left: 48px; top: 92px; display: flex; align-items: center; gap: 16px; }
  .brand-square { width: 34px; height: 34px; background: var(--accent-blue); }
  .brand-name { font-size: 40px; font-weight: 700; color: var(--ink-dark); letter-spacing: 0.5px; }

  .photo-grid { position: absolute; left: 32px; top: 252px; width: 810px; height: 712px; }
  .tile { position: absolute; }
  .tile-carved-hut {
    left: 0; top: 0; width: 400px; height: 362px;
    background: radial-gradient(ellipse at 45% 50%, #8a8478 0%, #6c665c 45%, #514b43 100%);
  }
  .tile-headline {
    left: 412px; top: 0; width: 398px; height: 362px;
    background: linear-gradient(160deg, var(--panel-dark), var(--panel-darker));
    padding: 58px 30px 0 34px; color: var(--white);
  }
  .tile-stone-arch {
    left: 0; top: 374px; width: 400px; height: 338px;
    background: linear-gradient(180deg, #6f7a5c 0%, #8b7d66 45%, #7a4d35 100%);
  }
  .tile-window-wall {
    left: 412px; top: 374px; width: 398px; height: 338px;
    background: linear-gradient(180deg, #5e4a3a 0%, #7c776f 35%, #8e8a82 70%, #a19c90 100%);
  }

  .headline { font-weight: 700; line-height: 1.12; }
  .headline-line { display: block; font-size: 42px; letter-spacing: -0.5px; }
  .headline-big { display: block; font-size: 66px; font-weight: 800; letter-spacing: -1.5px; margin-top: 4px; }
  .headline-note { margin-top: 10px; font-size: 22px; font-weight: 700; color: var(--accent-blue); }

  .signup-band {
    position: absolute; left: 32px; top: 988px; width: 810px; height: 142px;
    background: linear-gradient(180deg, var(--band-blue), var(--band-blue-dark));
    color: var(--white); text-align: center; padding-top: 30px;
  }
  .signup-text { font-size: 26px; font-weight: 600; }
  .signup-url { margin-top: 8px; font-size: 38px; font-weight: 700; letter-spacing: -0.3px; }
</style>
</head>
<body>
  <div class="poster">
    <header class="poster-header">
      <div class="brand">
        <span class="brand-square"></span>
        <span class="brand-name">Korvane Concrete Supply</span>
      </div>
    </header>

    <section class="photo-grid">
      <div class="tile tile-carved-hut" role="img" aria-label="Photo of a carved concrete hut with a textured conical roof, with a worker carving beside it"></div>
      <div class="tile tile-headline">
        <h1 class="headline">
          <span class="headline-line">We're hosting a</span>
          <span class="headline-line">vertical carving</span>
          <span class="headline-big">workshop.</span>
        </h1>
        <p class="headline-note">Details to be announced.</p>
      </div>
      <div class="tile tile-stone-arch" role="img" aria-label="Photo of a carved concrete stone arch in a garden with red mulch and plants"></div>
      <div class="tile tile-window-wall" role="img" aria-label="Photo of a carved stone-look concrete wall around a basement window with a timber beam above"></div>
    </section>

    <footer class="signup-band">
      <p class="signup-text">Sign up for more information</p>
      <p class="signup-url">www.korvaneconcrete.com/home.php</p>
    </footer>
  </div>
</body>
</html>
```